Larkspire Invitation

Please have the invitation say this
You're Invited to Our End-of-Summer Soirée!

As the summer winds down, we’d love for you to join us for a special evening of networking and good company, hosted by Larkspire Realty and Marcus Oyelaran with Tidewell Mortgage Solutions.

Date: September 19th, 2024
Time: 4:00 PM - 6:00 PM
Location: The Quillmere by Averett Boston Downtown, Fernvale Kitchen and Bar

We’re offering complimentary drinks, light bites, and an exciting raffle with a fantastic prize up for grabs! So come unwind, connect with fellow professionals, and enjoy a relaxing time together.

We can’t wait to see you there and share a toast to new opportunities!

Please RSVP by September 5th by emailing nadia@larkspireboston-mail.test

Please include the Quillmere Hotel Logo, Larkspire Logo and Tidewell Mortgage Solutions Logo. This should be a very classy invitation using navy and gold colors. Possibly herringbone pattern and aesthetic

```html
<!DOCTYPE html>
<html lang="en">
<head>
<meta charset="utf-8">
<title>Larkspire Invitation</title>
<link rel="stylesheet" href="https://fonts.googleapis.com/css2?family=Cormorant+Garamond:wght@400;500;600&display=swap">
<style>
  :root {
    --navy: #24344f;
    --gold-light: #f3c483;
    --gold-dark: #c09254;
    --gold-text: #d6a767;
    --muted: #5e6b82;
    --paper: #ffffff;
  }
  * { margin: 0; padding: 0; box-sizing: border-box; }
  html, body { width: 910px; height: 1200px; overflow: hidden; background: var(--paper); }
  body { position: relative; font-family: "Cormorant Garamond", Georgia, serif; color: var(--gold-text); }

  .invitation { position: absolute; left: 67px; top: 66px; width: 776px; height: 1058px; background: var(--navy); }
  .gold-band { position: absolute; left: 20px; top: 18px; right: 20px; bottom: 18px;
    background: linear-gradient(180deg, var(--gold-light), var(--gold-dark)); }
  .inner-panel { position: absolute; left: 40px; top: 38px; right: 40px; bottom: 38px; background: var(--navy); }
  .inner-rule { position: absolute; left: 49px; top: 47px; right: 49px; bottom: 47px;
    border: 2px solid; border-image: linear-gradient(180deg, var(--gold-light), var(--gold-dark)) 1; }

  .line { position: absolute; left: 0; width: 910px; text-align: center; white-space: nowrap; }

  .brand-ring { position: absolute; left: 418px; top: 143px; width: 76px; height: 76px;
    border: 3px solid #eebd7c; border-radius: 50%; }
  .brand-name { top: 220px; font-size: 30px; font-weight: 500; letter-spacing: 0.02em; color: #eebd7c; }
  .brand-sub { top: 250px; font-size: 12px; font-weight: 500; letter-spacing: 1.05em; color: #eebd7c; text-indent: 1.05em; }

  .headline { font-size: 80px; font-weight: 500; line-height: 1; letter-spacing: -0.01em; }
  .headline-1 { top: 290px; color: #ebbd7e; }
  .headline-2 { top: 370px; color: #e3b374; }
  .headline-3 { top: 449px; color: #d9a96a; }

  .divider { position: absolute; left: 417px; top: 544px; width: 83px; height: 2px; background: var(--gold-text); }

  .copy { font-size: 16px; line-height: 21.7px; letter-spacing: 0.045em; color: #d8aa6c; }
  .intro { top: 570px; }
  .event-date { top: 667px; font-size: 50px; font-weight: 500; line-height: 1; color: #d2a263; letter-spacing: -0.01em; }
  .event-date sup { font-size: 18px; vertical-align: 26px; margin-left: 1px; }
  .event-time { top: 719px; font-size: 18px; letter-spacing: 0.06em; color: #cfa064; }
  .venue { top: 767px; font-size: 17px; font-weight: 500; letter-spacing: 0.3em; color: #cfa064; }
  .venue-room { top: 794px; font-size: 16px; letter-spacing: 0.1em; color: #cd9e62; }
  .details { top: 826px; }
  .toast { top: 907px; }
  .rsvp { top: 939px; }

  .partner-ring { position: absolute; left: 350px; top: 990px; width: 60px; height: 60px;
    border: 1.5px solid var(--muted); border-radius: 50%; }
  .partner-name { position: absolute; left: 350px; top: 1054px; width: 60px; text-align: center;
    font-size: 9px; line-height: 11px; color: var(--muted); white-space: normal; }
  .hotel-name { position: absolute; left: 424px; top: 1000px; font-size: 34px; font-weight: 500;
    color: var(--muted); line-height: 1; }
  .hotel-sub { position: absolute; left: 441px; top: 1038px; font-size: 10px; font-weight: 500;
    letter-spacing: 0.2em; color: var(--muted); }
</style>
</head>
<body>
  <div class="invitation">
    <div class="gold-band"></div>
    <div class="inner-panel"></div>
    <div class="inner-rule"></div>
  </div>

  <div class="brand-ring"></div>
  <div class="line brand-name">LARKSPIRE</div>
  <div class="line brand-sub">REALTY</div>

  <h1>
    <span class="line headline headline-1">END</span>
    <span class="line headline headline-2">OF SUMMER</span>
    <span class="line headline headline-3">SOIRÉE</span>
  </h1>

  <div class="divider"></div>

  <p class="line copy intro">As the summer winds down, we’d love for you to join us for<br>a special evening of networking and good company, hosted by<br>Larkspire Realty and Marcus Oyelaran with Tidewell Mortgage Solutions.</p>

  <p class="line event-date">THU . 19<sup>th</sup>.&nbsp; SEP</p>
  <p class="line event-time">4:00 PM - 6:00 PM</p>

  <p class="line venue">The Quillmere by Averett Boston Downtown</p>
  <p class="line venue-room">Fernvale Kitchen and Bar</p>

  <p class="line copy details">We’re offering complimentary drinks, light bites, and an exciting<br>raffle with a fantastic prize up for grabs! So come unwind,<br>connect with fellow professionals, and enjoy a relaxing time together.</p>
  <p class="line copy toast">We can’t wait to see you there and share a toast to new opportunities!</p>
  <p class="line copy rsvp">Please RSVP by September 5th by emailing nadia@larkspireboston-mail.test</p>

  <div class="partner-ring"></div>
  <div class="partner-name">Tidewell</div>
  <div class="hotel-name">quillmere</div>
  <div class="hotel-sub">BY AVERETT</div>
</body>
</html>
```